Local Swedish accounting firm needs a webpage design.

We need a logo design for an accounting firm based in Malmö, Sweden called "Veltrana". We provide a full range of accounting services and have worked closely with startups for many years.
We would like to see an design using the following color scheme.
https://huepiq.io/9b90ba-bfae48-646f58-2541b2-d56501
The design should communicate ease of use and financial safety.

Target Market(s)

We are an accounting firm so are clients are startups and small to medium sized companys

Industry/Entity Type

Accounting

Coding

Coded - Design and coding required

Number of Pages Required

1 page

Font styles to use
Sans Serif

```html
<!DOCTYPE html>
<html lang="en">
<head>
<meta charset="utf-8">
<title>Veltrana – Accounting in Malmö</title>
<link href="https://fonts.googleapis.com/css2?family=Anton&family=Poppins:wght@300;400;500;600;700&display=swap" rel="stylesheet">
<style>
:root{
  --orange:#d56501;
  --orange-bright:#ef8300;
  --lavender:#9b90ba;
  --lavender-soft:#ece9f4;
  --gold:#bfae48;
  --olive:#646f58;
  --olive-dark:#2b3026;
  --blue:#2541b2;
  --ink:#222222;
  --text:#555555;
  --muted:#8a8a8a;
  --light:#f5f4f8;
  --line:#d9d5e6;
  --white:#ffffff;
}
*{margin:0;padding:0;box-sizing:border-box}
html,body{width:1200px;height:3780px;overflow:hidden}
body{font-family:"Poppins",sans-serif;color:var(--text);background:var(--white);position:relative;font-size:13px}
.abs{position:absolute}
.btn{display:inline-block;background:var(--orange);color:var(--white);font-weight:600;font-size:12px;letter-spacing:1px;text-transform:uppercase;padding:11px 26px;border-radius:22px;box-shadow:0 4px 10px rgba(213,101,1,.3)}
.brand{font-weight:700;color:var(--ink);font-size:22px;display:flex;align-items:center;gap:10px}
.brand-dot{width:14px;height:14px;background:var(--orange);border-radius:50%}

/* header */
.site-header{left:0;top:0;width:1200px;height:110px;background:var(--white);box-shadow:0 2px 10px rgba(0,0,0,.06)}
.site-header .brand{position:absolute;left:40px;top:30px}
.topbar{position:absolute;right:40px;top:12px;display:flex;gap:18px;align-items:center;font-size:12px;color:var(--olive)}
.topbar .pill{background:var(--orange);color:#fff;padding:5px 14px;border-radius:14px;font-weight:500;display:flex;gap:6px;align-items:center;white-space:nowrap}
.topbar .pill.login{background:var(--blue)}
.main-nav{position:absolute;left:460px;top:62px;display:flex;gap:30px;font-size:13px;color:var(--ink);font-weight:500;white-space:nowrap}
.main-nav .active{color:var(--orange);border-bottom:2px solid var(--orange);padding-bottom:4px}

/* hero */
.hero{left:0;top:110px;width:1200px;height:540px;background:linear-gradient(110deg,#d9c3a6 0%,#b98a5a 35%,#7a6f5e 62%,#4e5548 100%)}
.hero-copy{position:absolute;right:160px;top:140px;text-align:right}
.hero-copy h1{font-family:"Anton",sans-serif;font-weight:400;font-size:46px;line-height:1.15;color:#fff;letter-spacing:1px;text-shadow:0 3px 8px rgba(0,0,0,.35)}
.hero-copy h1 .hl{color:var(--orange-bright)}
.hero-copy p{color:#fff;font-size:17px;margin:14px 0 22px}

/* services */
.eyebrow{color:var(--lavender);font-size:14px;font-weight:500;text-align:center}
.section-title{color:var(--ink);font-size:34px;font-weight:500;text-align:center}
.section-title .hl{color:var(--orange)}
.services-head{left:0;top:800px;width:1200px}
.services-head .rule{width:60px;height:3px;background:var(--gold);margin:8px auto 0}
.service-grid{left:192px;top:900px;width:824px;display:grid;grid-template-columns:repeat(3,256px);gap:20px 28px}
.service-card{height:240px;background:#fff;box-shadow:0 4px 16px rgba(37,65,178,.1);border-bottom:3px solid var(--orange);padding:24px 22px;position:relative}
.service-card .icon{width:44px;height:44px;border-radius:6px;background:linear-gradient(135deg,var(--lavender),var(--blue))}
.service-card:nth-child(even) .icon{background:linear-gradient(135deg,var(--gold),var(--olive))}
.service-card h3{font-size:15px;font-weight:600;color:var(--ink);margin:14px 0 8px}
.service-card p{font-size:11px;line-height:1.6;color:var(--muted)}
.service-card .more{position:absolute;right:22px;bottom:18px;color:var(--blue);font-size:11px;font-weight:600}

/* about */
.about{left:0;top:1540px;width:1200px;height:570px;background:var(--light)}
.about-photo{position:absolute;right:0;top:0;width:390px;height:570px;background:linear-gradient(160deg,#2f3a66,#141a33)}
.about-circle{position:absolute;left:560px;top:130px;width:310px;height:310px;border-radius:50%;border:8px solid var(--orange);background:linear-gradient(135deg,#c9b8a4,#6a7788)}
.about-copy{position:absolute;left:160px;top:70px;width:360px}
.about-copy .eyebrow{text-align:left}
.about-copy h2{font-size:28px;color:var(--ink);font-weight:600}
.about-copy h4{font-size:14px;color:var(--olive);font-weight:500;margin:6px 0 12px}
.about-copy p{font-size:11.5px;line-height:1.7;margin-bottom:10px}
.about-list{list-style:none;margin:16px 0 24px}
.about-list li{font-size:12px;color:var(--ink);margin-bottom:10px;display:flex;align-items:center;gap:10px}
.about-list li::before{content:"";width:8px;height:8px;background:var(--gold);border-radius:50%}

/* entrepreneurs */
.entre-head{left:0;top:2210px;width:1200px}
.entre-grid{left:160px;top:2300px;display:flex;gap:26px}
.entre-card{width:200px}
.entre-card .pic{height:160px;border-radius:4px}
.entre-card h5{font-size:13px;font-weight:500;color:var(--ink);margin-top:14px;line-height:1.4;padding-left:10px;border-left:3px solid var(--lavender)}

/* callout */
.callout{left:0;top:2640px;width:1200px;height:240px;background:linear-gradient(90deg,var(--orange),var(--orange-bright))}
.callout h2{position:absolute;left:160px;top:64px;color:#fff;font-size:28px;font-weight:600}
.callout p{position:absolute;left:160px;top:118px;width:520px;color:#fff;font-size:12px;line-height:1.7;opacity:.92}
.call-box{position:absolute;left:760px;top:64px;width:300px;height:110px;border:2px solid rgba(255,255,255,.7);border-radius:8px;display:flex;align-items:center;gap:18px;padding:0 22px;color:#fff}
.call-box .ph{width:56px;height:56px;background:#fff;border-radius:8px;display:flex;align-items:center;justify-content:center;flex:none}
.call-box small{font-size:12px;display:block}
.call-box strong{font-size:26px;font-weight:700;white-space:nowrap;display:block;line-height:1.2}

/* contact */
.contact-head{left:0;top:2925px;width:1200px}
.contact-head p{text-align:center;font-size:12px;color:var(--text);margin-top:6px}
.contact-person{left:250px;top:3000px;width:260px;height:330px;border-radius:130px 130px 10px 10px;background:linear-gradient(180deg,var(--lavender-soft),#7f8fc9)}
.contact-form{left:600px;top:3030px;width:340px;display:flex;flex-direction:column;gap:14px}
.field{height:42px;border:1px solid var(--line);border-radius:3px;padding:12px 14px;font-size:12px;color:var(--muted)}
.field.msg{height:90px}
.contact-form .btn{align-self:flex-start;margin-top:4px}

/* footer */
.site-footer{left:0;top:3380px;width:1200px;height:400px;background:var(--olive-dark);color:#d6d8d0}
.site-footer .brand{position:absolute;left:160px;top:100px;color:#fff;font-size:26px}
.footer-col{position:absolute;top:70px}
.footer-col h6{color:var(--gold);font-size:13px;font-weight:600;letter-spacing:1px;text-transform:uppercase;margin-bottom:16px}
.footer-col ul{list-style:none}
.footer-col li{font-size:11.5px;margin-bottom:9px;display:flex;align-items:center;gap:8px}
.footer-col li::before{content:"";width:5px;height:5px;background:var(--orange);border-radius:50%;flex:none}
.footer-col.info li::before{display:none}
.footer-col .ic{width:26px;height:26px;border-radius:50%;background:var(--orange);flex:none}
.social{position:absolute;left:160px;top:160px;display:flex;gap:10px}
.social span{width:26px;height:26px;border-radius:50%;border:1px solid var(--lavender)}
.copy{position:absolute;left:0;bottom:0;width:1200px;height:44px;border-top:1px solid #3d4437;text-align:center;line-height:44px;font-size:11px;color:#a3a89a}
.copy b{color:var(--gold);font-weight:500}
</style>
</head>
<body>

<header class="abs site-header">
  <div class="brand"><span class="brand-dot"></span>Veltrana</div>
  <div class="topbar">
    <span>English</span>
    <span class="pill">
      <svg width="12" height="12" viewBox="0 0 24 24"><path fill="#fff" d="M6.6 10.8a15 15 0 0 0 6.6 6.6l2.2-2.2c.3-.3.7-.4 1-.2 1.1.4 2.3.6 3.6.6.6 0 1 .4 1 1V20c0 .6-.4 1-1 1A17 17 0 0 1 3 4c0-.6.4-1 1-1h3.5c.6 0 1 .4 1 1 0 1.3.2 2.5.6 3.6.1.3 0 .7-.2 1z"/></svg>
      040-55 2190</span>
    <span class="pill login">Client Login</span>
  </div>
  <nav class="main-nav">
    <span class="active">Home</span><span>Our Services</span><span>About Us</span><span>For Entrepreneurs</span><span>SERB</span><span>Get Started</span><span>Contact Us</span>
  </nav>
</header>

<section class="abs hero" role="img" aria-label="Smiling accountant with glasses working at a laptop in a bright office">
  <div class="hero-copy">
    <h1>Commitment<br><span class="hl">Holistic Perspective</span><br>Flexibility</h1>
    <p>Financial Control In The Steering Wheel Direction</p>
    <span class="btn">Contact Us</span>
  </div>
</section>

<div class="abs services-head">
  <p class="eyebrow">Why Choose Us</p>
  <h2 class="section-title">Our Services</h2>
  <div class="rule"></div>
</div>

<div class="abs service-grid">
  <article class="service-card"><div class="icon" role="img" aria-label="Accounting icon"></div><h3>Accounting</h3><p>We keep your books in order each month so you always know where your business stands today.</p><span class="more">Read More »</span></article>
  <article class="service-card"><div class="icon" role="img" aria-label="Payroll icon"></div><h3>Payroll Management</h3><p>Salaries, taxes and reports handled on time, so your team is paid right every month.</p><span class="more">Read More »</span></article>
  <article class="service-card"><div class="icon" role="img" aria-label="Project accounting icon"></div><h3>Project Accounting</h3><p>Follow cost and income per project with clear reports that help you plan ahead.</p><span class="more">Read More »</span></article>
  <article class="service-card"><div class="icon" role="img" aria-label="Annual accounts icon"></div><h3>Annual Accounts &amp; Declarations</h3><p>Year-end closing and tax returns prepared with care and filed on time.</p><span class="more">Read More »</span></article>
  <article class="service-card"><div class="icon" role="img" aria-label="Financial management icon"></div><h3>Financial management</h3><p>Budgets, forecasts and cash flow advice that keep your company safe and growing.</p><span class="more">Read More »</span></article>
  <article class="service-card"><div class="icon" role="img" aria-label="Finance department icon"></div><h3>Finance department</h3><p>A complete outsourced finance team that works as part of your company.</p><span class="more">Read More »</span></article>
</div>

<span class="abs btn" style="left:531px;top:1446px">Contact Us</span>

<section class="abs about">
  <div class="about-photo" role="img" aria-label="Colleagues reviewing charts in a dark office"></div>
  <div class="about-circle" role="img" aria-label="Two advisers discussing figures at a laptop"></div>
  <div class="about-copy">
    <p class="eyebrow">About Us</p>
    <h2>Veltrana</h2>
    <h4>Financial Control In The Steering Wheel Direction</h4>
    <p>Veltrana helps startups and growing companies in Malmö with accounting that is simple, clear and safe, so owners can focus on the business ahead.</p>
    <p>We give you a trusted partner with the expertise to keep your figures right and the overview you need to steer with confidence.</p>
    <ul class="about-list">
      <li>Business System</li><li>Consulting</li><li>Taken Advantage</li><li>Chief Financial Officer / Controller</li>
    </ul>
    <span class="btn">Learn More</span>
  </div>
</section>

<div class="abs entre-head">
  <h2 class="section-title"><span class="hl">For</span> Entrepreneurs</h2>
</div>
<div class="abs entre-grid">
  <div class="entre-card"><div class="pic" role="img" aria-label="Hands working on documents" style="background:linear-gradient(135deg,#e7d9c8,#9c7f62)"></div><h5>Stable Basic Structure</h5></div>
  <div class="entre-card"><div class="pic" role="img" aria-label="Team reviewing financial papers" style="background:linear-gradient(135deg,#c6cdea,#2541b2)"></div><h5>Help Interpret Financial Information</h5></div>
  <div class="entre-card"><div class="pic" role="img" aria-label="Calculator and charts on a desk" style="background:linear-gradient(135deg,#e6dca0,#bfae48)"></div><h5>Adapts the Accounting According To The Development Phase</h5></div>
  <div class="entre-card"><div class="pic" role="img" aria-label="Adviser answering questions at a desk" style="background:linear-gradient(135deg,#dcd8e8,#9b90ba)"></div><h5>We Are Happy To Answer Your Questions</h5></div>
</div>

<section class="abs callout">
  <h2>Looking For Accounting Services ?</h2>
  <p>Are you an entrepreneur with questions about accounting and financial planning? We listen to your plans and find a solution that fits, so you can grow with control and peace of mind.</p>
  <div class="call-box">
    <div class="ph"><svg width="28" height="28" viewBox="0 0 24 24"><path fill="#d56501" d="M6.6 10.8a15 15 0 0 0 6.6 6.6l2.2-2.2c.3-.3.7-.4 1-.2 1.1.4 2.3.6 3.6.6.6 0 1 .4 1 1V20c0 .6-.4 1-1 1A17 17 0 0 1 3 4c0-.6.4-1 1-1h3.5c.6 0 1 .4 1 1 0 1.3.2 2.5.6 3.6.1.3 0 .7-.2 1z"/></svg></div>
    <div><small>Call Us On</small><strong>040-55 2190</strong></div>
  </div>
</section>

<div class="abs contact-head">
  <h2 class="section-title">Contact <span class="hl">Us</span></h2>
  <p>Have An Any Question Please Contact Us Today !</p>
</div>
<div class="abs contact-person" role="img" aria-label="Smiling man sitting with a laptop, gesturing to the form"></div>
<form class="abs contact-form">
  <div class="field">Name *</div>
  <div class="field">Email *</div>
  <div class="field">Phone *</div>
  <div class="field msg">Message *</div>
  <span class="btn">Send Us</span>
</form>

<footer class="abs site-footer">
  <div class="brand"><span class="brand-dot"></span>Veltrana</div>
  <div class="social"><span></span><span></span></div>
  <div class="footer-col" style="left:400px">
    <h6>Sitemap</h6>
    <ul><li>Home</li><li>Our Services</li><li>About Us</li><li>For Entrepreneurs</li><li>SERB</li><li>Get Started</li><li>Contact Us</li></ul>
  </div>
  <div class="footer-col" style="left:610px">
    <h6>Services</h6>
    <ul><li>Accounting</li><li>Payroll Management</li><li>Annual Accounts &amp; Declarations</li><li>Project Accounting</li><li>Financial management</li><li>Finance department</li></ul>
  </div>
  <div class="footer-col info" style="left:840px">
    <h6>Contact Info</h6>
    <ul>
      <li><span class="ic"></span>Veltrana AB<br>Hamngatan 14, 211 22 Malmö</li>
      <li><span class="ic"></span>040-55 2190</li>
      <li><span class="ic"></span>info@veltrana.se</li>
    </ul>
  </div>
  <div class="copy">© <b>Veltrana</b> 2024. All rights reserved.</div>
</footer>

</body>
</html>
```